Copperleaf Motorized Shade Business Card

Hello, we've had our logo made. Now we are looking for a clean and cool looking business card. One side can just be the logo with any design elements that might look good with it. The other side will be Name, Phone Number and Email. There will not be an address on the card.

```html
<!DOCTYPE html>
<html lang="en">
<head>
<meta charset="utf-8">
<title>Copperleaf Motorized Shade Business Card</title>
<link rel="stylesheet" href="https://fonts.googleapis.com/css2?family=Oswald:wght@600&family=Montserrat:wght@400;500&display=swap">
<style>
  :root {
    --stage: #f3d678;
    --sun: #f8c22c;
    --navy: #1f4c86;
    --navy-deep: #0d3468;
    --navy-soft: #3a6396;
    --white: #ffffff;
  }
  html, body {
    margin: 0;
    width: 1200px;
    height: 800px;
    overflow: hidden;
    background: var(--stage);
  }
  .sheet {
    width: 1200px;
    height: 800px;
    display: flex;
    align-items: center;
    justify-content: center;
    gap: 60px;
  }
  .card {
    position: relative;
    width: 520px;
    height: 297px;
    overflow: hidden;
    box-shadow: 0 18px 40px rgba(120, 90, 10, 0.28);
  }
  .card-front { background: var(--sun); }
  .card-back {
    background: linear-gradient(150deg, var(--navy-soft) 0%, var(--navy) 45%, var(--navy-deep) 100%);
    display: flex;
    align-items: center;
    justify-content: center;
  }
  .photo-panel {
    position: absolute;
    left: 0;
    top: 0;
    width: 250px;
    height: 297px;
    background: linear-gradient(160deg, var(--navy-soft) 0%, var(--navy) 55%, var(--navy-deep) 100%);
    clip-path: polygon(0 0, 62% 0, 100% 100%, 0 100%);
  }

  .contact-block {
    position: absolute;
    right: 28px;
    top: 58px;
    width: 210px;
    color: var(--navy);
  }
  .holder-name {
    margin: 0;
    font-family: "Oswald", sans-serif;
    font-weight: 600;
    font-size: 42px;
    line-height: 1;
    letter-spacing: -0.5px;
    text-transform: uppercase;
  }
  .holder-role {
    margin: 4px 0 0;
    font-family: "Montserrat", sans-serif;
    font-weight: 500;
    font-size: 12px;
    letter-spacing: 0.8px;
    text-transform: uppercase;
  }
  .contact-list {
    list-style: none;
    margin: 20px 0 0 6px;
    padding: 0 0 0 12px;
    border-left: 1px solid var(--navy);
    font-family: "Montserrat", sans-serif;
    font-size: 11px;
  }
  .contact-list li {
    display: flex;
    align-items: center;
    gap: 8px;
    margin: 6px 0;
    white-space: nowrap;
  }
  .contact-icon { width: 16px; height: 16px; flex: none; }

  .brand-small {
    position: absolute;
    left: 34px;
    bottom: 26px;
    font-family: "Oswald", sans-serif;
    font-weight: 600;
    font-size: 13px;
    line-height: 1.1;
    color: var(--white);
    text-transform: uppercase;
    letter-spacing: 0.5px;
  }
  .brand-large {
    font-family: "Oswald", sans-serif;
    font-weight: 600;
    color: var(--white);
    text-transform: uppercase;
    text-align: center;
    line-height: 1.05;
  }
  .brand-large .brand-name { display: block; font-size: 40px; letter-spacing: 1px; }
  .brand-large .brand-line { display: block; font-size: 15px; letter-spacing: 4px; }
</style>
</head>
<body>
<main class="sheet">

  <section class="card card-front" aria-label="Business card, contact side">
    <div class="photo-panel" role="img" aria-label="Blue-toned architectural photo of a building facade"></div>

    <div class="brand-small">Copperleaf<br>Motorized Shade</div>

    <div class="contact-block">
      <h1 class="holder-name">Name Here</h1>
      <p class="holder-role">Account Manager</p>
      <ul class="contact-list">
        <li>
          <svg class="contact-icon" viewBox="0 0 16 16" aria-hidden="true">
            <circle cx="8" cy="8" r="8" fill="var(--navy)"/>
            <path fill="var(--sun)" d="M5 4.2l1.4-.3.8 1.9-.9.7c.5 1.1 1.3 1.9 2.4 2.4l.7-.9 1.9.8-.3 1.4c-3.3.2-6.3-2.8-6-6z"/>
          </svg>
          <span>+00 999 999 999</span>
        </li>
        <li>
          <svg class="contact-icon" viewBox="0 0 16 16" aria-hidden="true">
            <circle cx="8" cy="8" r="8" fill="var(--navy)"/>
            <rect x="4" y="5.2" width="8" height="5.6" fill="none" stroke="var(--sun)" stroke-width="1"/>
            <path d="M4 5.4l4 3 4-3" fill="none" stroke="var(--sun)" stroke-width="1"/>
          </svg>
          <span>news@yourcompany.com</span>
        </li>
      </ul>
    </div>
  </section>

  <section class="card card-back" aria-label="Business card, brand side">
    <div class="brand-large">
      <span class="brand-name">Copperleaf</span>
      <span class="brand-line">Motorized Shade</span>
    </div>
  </section>

</main>
</body>
</html>
```